New Body Mist 250 ml exclusive

We are excited to embark on a new project to design the packaging for body mist:
Amber Drizzle

We are looking for a design that is truly unique and stands out, with a touch of individuality that sets it apart. The design should be eye-catching and visually appealing, drawing attention even from a distance. We want the body mists to have a fun and attractive look that appeals to customers.

To help bring your design to life, we will provide the dimensions of the bottle, which has a capacity of 250ml. The bottle measures 13.3 cm in height and 4.9 cm in diameter (excluding the pump). Additionally, we will also provide the dimensions of the label, which measures 15.1 cm in height and 12.8 cm in width.

We believe that giving you the freedom to put your own unique touch and color choices will help create a truly standout design. We look forward to seeing your creative vision for our body mist.

We shared with you the logo of the body mist and some examples of models that we liked.

Please be informed that the project only includes one design and the remaining three will be completed and paid for through a 1on1 project with the winner of the contest.

Target Market(s)

Supermarket and perfumery stores

Industry/Entity Type

Cosmetics

Font styles to use
Serif

Requirements
Must have
• Uniqueness and attractiveness

```html
<!DOCTYPE html>
<html lang="en">
<head>
<meta charset="utf-8">
<title>Amber Drizzle – Soft Grace Fragrance Mist Label</title>
<link href="https://fonts.googleapis.com/css2?family=Josefin+Sans:wght@400&family=Great+Vibes&family=Cabin:wght@400&family=Open+Sans:wght@600&display=swap" rel="stylesheet">
<style>
  :root {
    --page-bg: #ffffff;
    --plum: #27063d;
    --blush-text: #f6cdca;
    --marble: #f3e2e3;
    --marble-vein: #ecd3d1;
    --band-start: #5a1a6b;
    --band-end: #9b169f;
    --band-text: #fbeef6;
    --ink: #2a0a3e;
  }
  * { margin: 0; padding: 0; box-sizing: border-box; }
  html, body {
    width: 1200px;
    height: 1156px;
    overflow: hidden;
    background: var(--page-bg);
  }
  .canvas {
    position: relative;
    width: 1200px;
    height: 1156px;
  }
  .label {
    position: absolute;
    left: 410px;
    top: 68px;
    width: 380px;
    height: 1020px;
    overflow: hidden;
    background:
      radial-gradient(ellipse at 20% 60%, var(--marble-vein) 0%, transparent 35%),
      radial-gradient(ellipse at 80% 85%, var(--marble-vein) 0%, transparent 30%),
      var(--marble);
  }
  .label-top {
    position: absolute;
    left: 0; top: 0;
    width: 100%;
    height: 419px;
    background: var(--plum);
  }
  .brand-name {
    position: absolute;
    top: 50px;
    width: 100%;
    text-align: center;
    font-family: "Josefin Sans", sans-serif;
    font-weight: 400;
    font-size: 58px;
    line-height: 58px;
    letter-spacing: 5px;
    text-transform: uppercase;
    color: var(--blush-text);
  }
  .flower-art {
    position: absolute;
    left: 0;
    top: 211px;
    width: 100%;
    height: 313px;
  }
  .product-name {
    position: absolute;
    top: 548px;
    width: 100%;
    text-align: center;
    font-family: "Great Vibes", cursive;
    font-weight: 400;
    font-size: 92px;
    line-height: 78px;
    color: var(--ink);
  }
  .tagline {
    position: absolute;
    top: 722px;
    width: 100%;
    text-align: center;
    font-family: "Cabin", sans-serif;
    font-size: 18px;
    line-height: 25px;
    color: var(--ink);
  }
  .range-band {
    position: absolute;
    left: 0;
    top: 823px;
    width: 100%;
    height: 83px;
    background: linear-gradient(90deg, var(--band-start) 0%, #6e2a7e 25%, var(--band-end) 80%, #7a1482 100%);
    display: flex;
    flex-direction: column;
    justify-content: center;
    align-items: center;
    font-family: "Open Sans", sans-serif;
    font-weight: 600;
    font-size: 23px;
    line-height: 31px;
    letter-spacing: 0.5px;
    color: var(--band-text);
  }
  .volume {
    position: absolute;
    top: 946px;
    width: 100%;
    text-align: center;
    font-family: "Cabin", sans-serif;
    font-size: 28px;
    line-height: 40px;
    color: var(--ink);
  }
</style>
</head>
<body>
<main class="canvas">
  <section class="label">
    <div class="label-top"></div>
    <h1 class="brand-name">Amber<br>Drizzle</h1>
    <svg class="flower-art" viewBox="0 0 380 313" role="img" aria-label="Illustration of a cream vanilla orchid flower lying on dark brown vanilla pods">
      <defs>
        <radialGradient id="bloomGlow" cx="45%" cy="50%" r="50%">
          <stop offset="0%" stop-color="#fbf6d8"/>
          <stop offset="55%" stop-color="#efe6c4"/>
          <stop offset="100%" stop-color="#efe6c4" stop-opacity="0"/>
        </radialGradient>
      </defs>
      <rect x="0" y="180" width="380" height="38" fill="#4a3424" opacity="0.85"/>
      <ellipse cx="175" cy="150" rx="150" ry="135" fill="url(#bloomGlow)"/>
    </svg>
    <h2 class="product-name">Soft<br>Grace</h2>
    <p class="tagline">Lorem text is just<br>for sampling text</p>
    <div class="range-band">
      <span>FRAGRANCE MIST</span>
      <span>HIDDEN MEADOWS</span>
    </div>
    <p class="volume">e 250 ml</p>
  </section>
</main>
</body>
</html>
```